Detailed Flyer for fence material

I need a large several page flyer that showcases all of the fence styles and designs, similar to the attached flyers here but with our name and branding for our business. There are 5 styles I want to showcase : Flat Top (Corvanne), Flat Top with Spear (Tursdale), Spear Top (Pomberly), Staggered Spear (Quimby) and 2 Rail (Ravo). I also need to show the picket configurations: standard picket, puppy picket, double picket. Attached are also photos that can be used on the flyer. Our website is www.GetMetalRailing.example - The business name is Bluegate Fence (logo is at www.ourvelmorefence.example). Please use the Harlow Fence brochure as a basis for the design - we need the information here but rebranded to Bluegate Fence.https://files.exampledocs.example/static/a1b2c3/Penwick+Decorative+Railing+Brochure+0917-2.pdf

Gates also need to be shown with different configurations for walk gate and double gates as shown on the harlow flyer.

Would prefer a one page flyer, but two page will be OK too.

Target Market(s)

Homeowners and Contractors (Landscapers, fence builders)

Industry/Entity Type

Construction

Font styles to use
Sans Serif
Other font styles liked:
• Arial

Colors
0054AA
0677BA
7BADD7
CADEEF
E8F1F8

Requirements
Must have
• Our aluminum fence styles and gate options
Nice to have
• Some photos of the fencing and the benefits of the material

```html
<!DOCTYPE html>
<html lang="en">
<head>
<meta charset="utf-8">
<title>Bluegate Fence – Aluminum Fence Styles Flyer</title>
<link href="https://fonts.googleapis.com/css2?family=Poppins:wght@400;500;600;700&family=Righteous&display=swap" rel="stylesheet">
<style>
  :root{
    --navy:#1b2d57;
    --orange:#f28a2c;
    --sky:#3a8bd2;
    --white:#ffffff;
    --ink:#1f2f5c;
    --text:#333a48;
    --stage:#dcdcdc;
    --drawing:rgba(255,255,255,.14);
  }
  *{margin:0;padding:0;box-sizing:border-box}
  html,body{width:893px;height:1200px;overflow:hidden;background:var(--stage)}
  .spread{position:relative;width:893px;height:1200px;overflow:hidden;font-family:"Poppins",Arial,sans-serif}
  .page{position:absolute;top:301px;width:662px;height:935px;overflow:hidden;transform:scale(.64);transform-origin:0 0;background:var(--navy)}
  .page-front{left:16px}
  .page-back{left:453px}
  .page-shapes{position:absolute;inset:0}

  /* front page */
  .intro{position:absolute;left:26px;top:26px;width:250px}
  .brand{display:flex;align-items:center;gap:10px}
  .brand-mark{width:18px;height:18px;border-radius:50%;background:var(--orange);flex:none}
  .brand-name{font-size:19px;font-weight:600;color:var(--sky);line-height:1}
  .brand-phone{font-family:"Righteous","Poppins",sans-serif;font-size:18px;color:var(--ink);margin:4px 0 0 28px;line-height:1}
  .brand-tagline{font-size:5.8px;font-weight:600;color:var(--ink);margin:4px 0 0 28px;white-space:nowrap}
  .headline{margin-top:30px;font-size:19px;font-weight:700;color:var(--ink);line-height:1.22;width:250px}
  .intro-copy{margin-top:10px;font-size:10.6px;line-height:1.27;color:var(--text);width:240px}
  .intro-copy + .intro-copy{margin-top:12px}
  .style-card{position:absolute;width:182px;text-align:center}
  .style-frame{width:182px;height:170px;background:var(--white);clip-path:polygon(50% 0,100% 24%,100% 100%,0 100%,0 24%);padding:6px}
  .style-photo{width:100%;height:100%;clip-path:polygon(50% 0,100% 24%,100% 100%,0 100%,0 24%);background:linear-gradient(180deg,#c9d6d0 0%,#6f8a5a 45%,#4c6a36 75%,#7a6a52 100%)}
  .style-name{margin-top:9px;font-size:14px;font-weight:500;color:var(--white);line-height:1.2;letter-spacing:.3px}
  .contact{position:absolute;left:36px;top:869px;color:var(--white);font-size:13.5px;font-weight:500;font-style:normal}
  .contact-line{display:flex;align-items:center;gap:9px;height:26px}
  .contact-line svg{width:17px;height:17px;flex:none}
  .cta{position:absolute;right:24px;top:853px;text-align:right;color:var(--white)}
  .cta-lead{font-size:16.5px;font-weight:500;letter-spacing:.3px}
  .cta-phone{font-family:"Righteous","Poppins",sans-serif;font-size:38px;line-height:1.1;letter-spacing:1px}

  /* back page */
  .section-title{position:absolute;left:0;width:662px;text-align:center;color:var(--white);font-size:16px;font-weight:500;letter-spacing:.2px}
  .config{position:absolute;text-align:center;color:var(--white)}
  .config-drawing{background:var(--drawing);width:100%}
  .config-name{font-size:14px;font-weight:600;margin-top:18px}
  .gate-name{font-size:8.5px;font-weight:600;margin-top:14px;line-height:1.2}
  .back-footer{position:absolute;left:0;top:757px;width:662px;height:178px;background:var(--sky);border-top:5px solid var(--white);color:var(--white)}
  .company{position:absolute;left:24px;top:28px;font-style:normal;font-size:13px;font-weight:600;line-height:16.3px}
  .company-name{font-size:15px;font-weight:700;display:block;margin-bottom:1px}
  .warranty{position:absolute;left:343px;top:30px;width:298px}
  .warranty-title{font-size:15px;font-weight:700;letter-spacing:.5px}
  .warranty-copy{margin-top:4px;font-size:8.6px;line-height:10.4px}
</style>
</head>
<body>
<main class="spread">

  <!-- Front page -->
  <section class="page page-front">
    <svg class="page-shapes" viewBox="0 0 662 935" width="662" height="935">
      <defs>
        <linearGradient id="navy-wash-front" x1="0" y1="0" x2="1" y2="1">
          <stop offset="0" stop-color="#21376a"/><stop offset=".5" stop-color="#1a2c56"/><stop offset="1" stop-color="#13244a"/>
        </linearGradient>
        <linearGradient id="hero-tones" x1="0" y1="0" x2="0" y2="1">
          <stop offset="0" stop-color="#3f5b34"/><stop offset=".4" stop-color="#5c7d3f"/><stop offset=".75" stop-color="#6f9a45"/><stop offset="1" stop-color="#4e7a30"/>
        </linearGradient>
      </defs>
      <rect width="662" height="935" fill="url(#navy-wash-front)"/>
      <polygon role="img" aria-label="Photo of a black aluminum picket fence with a gate post along a green lawn" points="208,0 662,0 662,290 440,350 288,280 288,0" fill="url(#hero-tones)"/>
      <polygon points="0,0 208,0 288,62 288,300 0,319" fill="#ffffff"/>
      <polygon points="256,300 288,290 440,350 662,290 662,318 440,380 256,318" fill="#f28a2c"/>
      <polygon points="0,319 113,359 0,424" fill="#f28a2c"/>
      <polygon points="533,374 662,309 662,429" fill="#3a8bd2"/>
      <rect x="0" y="859" width="662" height="76" fill="#3a8bd2"/>
      <polygon points="326,837 662,837 662,935 294,935" fill="#f28a2c"/>
    </svg>

    <div class="intro">
      <div class="brand"><span class="brand-mark"></span><span class="brand-name">Bluegate Fence</span></div>
      <div class="brand-phone">555-014-7720</div>
      <div class="brand-tagline">“Because Good Fences Make Good Neighbors”</div>
      <h1 class="headline">Ready for your new fence? Lets get started.</h1>
      <p class="intro-copy">From our 30+ years experience of building custom fencing solutions for homeowners and builders alike, we have learned how to provide specialized service to each customer of ours.</p>
      <p class="intro-copy">We pride ourselves on great work and know that our success can only be seen through the success of every fence and deck installation we complete.</p>
    </div>

    <figure class="style-card" style="left:36px;top:404px">
      <div class="style-frame"><div class="style-photo" role="img" aria-label="Photo of a flat top aluminum fence on a lawn"></div></div>
      <figcaption class="style-name">Flat Top (Corvanne)</figcaption>
    </figure>
    <figure class="style-card" style="left:240px;top:404px">
      <div class="style-frame"><div class="style-photo" role="img" aria-label="Photo of a flat top fence with spear pickets along a wooded yard"></div></div>
      <figcaption class="style-name">Flat Top with Spear<br>(Tursdale)</figcaption>
    </figure>
    <figure class="style-card" style="left:445px;top:404px">
      <div class="style-frame"><div class="style-photo" role="img" aria-label="Photo of a spear top aluminum fence beside a sidewalk"></div></div>
      <figcaption class="style-name">Spear Top (Pomberly)</figcaption>
    </figure>
    <figure class="style-card" style="left:140px;top:619px">
      <div class="style-frame"><div class="style-photo" role="img" aria-label="Photo of a staggered spear double gate in front of a house"></div></div>
      <figcaption class="style-name">Staggered Spear (Quimby)</figcaption>
    </figure>
    <figure class="style-card" style="left:343px;top:619px">
      <div class="style-frame"><div class="style-photo" role="img" aria-label="Photo of a two rail aluminum fence over mulch"></div></div>
      <figcaption class="style-name">2 Rail (Ravo)</figcaption>
    </figure>

    <address class="contact">
      <div class="contact-line">
        <svg viewBox="0 0 24 24" fill="none" stroke="#fff" stroke-width="2"><rect x="2" y="5" width="20" height="14" rx="1"/><path d="M2 6l10 7 10-7"/></svg>
        <span>www.ourvelmorefence.example</span>
      </div>
      <div class="contact-line">
        <svg viewBox="0 0 24 24" fill="none" stroke="#fff" stroke-width="2"><circle cx="12" cy="12" r="10"/><path d="M2 12h20M12 2c3 3 3 17 0 20M12 2c-3 3-3 17 0 20"/></svg>
        <span>office@ourvelmorefence.example</span>
      </div>
    </address>

    <div class="cta">
      <div class="cta-lead">Call us today for a free estimate</div>
      <div class="cta-phone">555-014-7720</div>
    </div>
  </section>

  <!-- Back page -->
  <section class="page page-back">
    <svg class="page-shapes" viewBox="0 0 662 935" width="662" height="935">
      <defs>
        <linearGradient id="navy-wash-back" x1="0" y1="0" x2="1" y2="1">
          <stop offset="0" stop-color="#21376a"/><stop offset=".5" stop-color="#1a2c56"/><stop offset="1" stop-color="#13244a"/>
        </linearGradient>
        <linearGradient id="install-tones" x1="0" y1="0" x2="0" y2="1">
          <stop offset="0" stop-color="#d7dde2"/><stop offset=".45" stop-color="#8e9aa6"/><stop offset=".75" stop-color="#6c8a4c"/><stop offset="1" stop-color="#4f7232"/>
        </linearGradient>
      </defs>
      <rect width="662" height="935" fill="url(#navy-wash-back)"/>
      <polygon role="img" aria-label="Photo of an installer fastening a tall aluminum fence panel" points="0,0 662,0 662,300 344,340 0,279" fill="url(#install-tones)"/>
      <polygon points="0,279 344,340 662,300 662,330 344,375 0,311" fill="#f28a2c"/>
    </svg>

    <h2 class="section-title" style="top:389px">Configurations for Picket</h2>
    <div class="config" style="left:34px;top:426px;width:190px">
      <div class="config-drawing" style="height:110px" role="img" aria-label="Line drawing of a standard picket panel"></div>
      <div class="config-name">Standard Picket</div>
    </div>
    <div class="config" style="left:241px;top:426px;width:188px">
      <div class="config-drawing" style="height:110px" role="img" aria-label="Line drawing of a puppy picket panel"></div>
      <div class="config-name">Puppy Picket</div>
    </div>
    <div class="config" style="left:446px;top:426px;width:190px">
      <div class="config-drawing" style="height:110px" role="img" aria-label="Line drawing of a double picket panel"></div>
      <div class="config-name">Double Picke</div>
    </div>

    <h2 class="section-title" style="top:583px">Configurations for walk gate and double gates</h2>
    <div class="config" style="left:27px;top:624px;width:70px">
      <div class="config-drawing" style="height:75px" role="img" aria-label="Line drawing of a straight top walkway gate"></div>
      <div class="gate-name">Straight Top<br>Walkway Gate</div>
    </div>
    <div class="config" style="left:109px;top:624px;width:71px">
      <div class="config-drawing" style="height:75px" role="img" aria-label="Line drawing of an arched top walkway gate"></div>
      <div class="gate-name">Arched Top<br>Walkway Gate</div>
    </div>
    <div class="config" style="left:194px;top:624px;width:138px">
      <div class="config-drawing" style="height:75px" role="img" aria-label="Line drawing of a rainbow arch double gate"></div>
      <div class="gate-name">Rainbow Arch Double Gate</div>
    </div>
    <div class="config" style="left:346px;top:624px;width:136px">
      <div class="config-drawing" style="height:75px" role="img" aria-label="Line drawing of an estate arch double gate"></div>
      <div class="gate-name">Estate Arch Double Gate</div>
    </div>
    <div class="config" style="left:496px;top:624px;width:138px">
      <div class="config-drawing" style="height:75px" role="img" aria-label="Line drawing of an arched double gate"></div>
      <div class="gate-name">Arched Double Gate</div>
    </div>

    <footer class="back-footer">
      <address class="company">
        <span class="company-name">Bluegate Fence, LLC</span>
        Phone: 555-014-7720<br>
        Email: office@ourvelmorefence.example<br>
        Website: www.ourvelmorefence.example<br>
        Address: 1187 Harrow Mill Rd,<br>
        Dalton Ridge NC 28990<br>
        Office hours: Monday - Friday: 9AM - 4PM<br>
        Saturday: 9AM - 12PM
      </address>
      <div class="warranty">
        <h3 class="warranty-title">WARRANTY</h3>
        <p class="warranty-copy">Bluegate Fence provides a lifetime warranty on all workmanship and labor. Aluminum fences have a limited lifetime warranty from the manufacturer. The manufacturer warrants that the materials will be free from defect in workmanship and that the coating will not crack, peel, chip or peel. The warranty does not extend to damage caused by other than that for which the material was designed, negligence, alteration, accident, improper storage, abuse, misuse, vandalism, or acts of God.</p>
      </div>
    </footer>
  </section>

</main>
</body>
</html>
```